Health Clinic treating people with mental illness needs a website

We need a website for a new mental health clinic based in Florida called Brightmoor Wellness USA. We treat people with mental health issues such as depression, PTSD, Bipolar, chronic pain, etc. I want the website to be easy to follow and inviting to the visitors. It should be easy to locate the different treatment options and how to go about contacting and making appointments. The images on the website should be something that the patients can relate to, whether a close up of a woman's face, something that conveys emotion. The patients visiting this website are often sad and miserable, they need to be able to feel comfortable when they look at this website. I want them to feel that we understand where they are coming from. I like colors such as purple, turquoise, lavender.

Target Market(s)

College students, veterans, anyone with mental illness

Industry/Entity Type

Health And Wellness

Font styles to use
Serif
Sans Serif

Colors

Designer to choose colors to be used in the design.

Requirements
Must have
• There should be a home/landing page, about us page, treatment page, contact page, and a FAQ page. I've included my logo below.
Nice to have
• The flow of the web pages should be calming and welcoming. I want people to feel warm and understood when they enter our page.
Should not have
• The images and writing should not be overly stimulating or aggressive.

```html
<!DOCTYPE html>
<html lang="en">
<head>
<meta charset="utf-8">
<title>Brightmoor Wellness USA</title>
<link href="https://fonts.googleapis.com/css2?family=Lora:ital,wght@0,400;0,600;1,700&family=Poppins:wght@400;500;600&display=swap" rel="stylesheet">
<style>
:root{
  --purple:#6a2c91;
  --purple-dark:#4f1f70;
  --violet:#7b3fb0;
  --green:#6cb51c;
  --green-dark:#5a9c12;
  --yellow:#f7d56a;
  --ink:#2b2b2b;
  --muted:#7a7a7a;
  --line:#e6e6e6;
  --white:#ffffff;
  --foot-top:#7c1f86;
  --foot-bot:#5a2f8f;
  --serif:'Lora', Georgia, serif;
  --sans:'Poppins', Arial, sans-serif;
}
*{box-sizing:border-box;margin:0;padding:0}
html,body{width:1200px;height:3409px;overflow:hidden}
body{position:relative;background:var(--white);font-family:var(--sans);color:var(--ink)}
.abs{position:absolute}
a{color:inherit;text-decoration:none}

/* hero */
.hero-photo{left:0;top:0;width:1200px;height:660px;
  background:
   radial-gradient(ellipse 260px 320px at 640px 300px,#c79a7c 0%,#a8745a 45%,rgba(120,80,70,0) 100%),
   linear-gradient(180deg,#f4f1ec 0%,#e3ddd0 14%,#b9a98a 32%,#8c7a64 52%,#6f5b73 72%,#5c4a6a 100%)}
.hero-wave{left:0;top:520px;width:1200px;height:145px}
.logo{left:152px;top:56px;display:flex;align-items:center;gap:8px}
.logo-name{font-family:var(--serif);font-weight:600;font-size:30px;color:var(--purple);line-height:1}
.logo-dot{width:12px;height:12px;border-radius:50%;background:var(--green)}
.logo-sub{left:190px;top:92px;font-size:11px;letter-spacing:2px;color:var(--green);font-weight:500}
.btn-top{left:906px;top:22px;width:138px;height:32px;border-radius:16px;background:var(--purple);color:#fff;font-size:9px;font-weight:600;display:flex;align-items:center;justify-content:center;letter-spacing:.5px}
.nav{left:546px;top:78px;display:flex;gap:0;font-family:var(--serif);font-size:11px;font-weight:600;color:#333}
.nav a{display:block;margin-right:38px;padding-bottom:6px}
.nav a.active{color:var(--purple);border-bottom:2px solid var(--purple)}
.hero-title{left:300px;top:410px;width:730px;text-align:right;font-family:var(--serif);font-style:italic;font-weight:700;font-size:40px;line-height:44px;color:#fff;text-shadow:0 2px 6px rgba(0,0,0,.45)}
.btn{height:38px;border-radius:19px;color:#fff;font-size:11px;font-weight:600;display:flex;align-items:center;justify-content:center}
.btn-know{left:662px;top:529px;width:176px;background:var(--green)}
.btn-book{left:850px;top:529px;width:176px;background:var(--violet)}

/* welcome */
.welcome-kicker{left:215px;top:630px;font-size:14px;color:var(--muted)}
.welcome-title{left:215px;top:647px;font-family:var(--serif);font-size:34px;color:var(--purple)}
.feature{top:711px;width:226px;height:316px;padding:24px 22px}
.feature .icon{width:46px;height:46px;border:2px solid var(--green);border-radius:4px;display:flex;align-items:center;justify-content:center}
.feature h3{margin-top:86px;font-size:13px;font-weight:500}
.feature p{margin-top:14px;font-size:11px;line-height:16px;color:var(--muted)}
.feature .arrow{position:absolute;left:22px;bottom:30px;font-size:14px}
.feature.is-active{background:var(--green);color:#fff}
.feature.is-active p{color:#f2ffe4}
.feature.is-active .icon{border-color:#fff}

/* appointment band */
.band{left:0;top:1105px;width:1200px;height:472px}
.band-kicker{font-family:var(--serif);font-size:15px;color:#fff}
.band-title{font-family:var(--serif);font-size:26px;color:#fff}
.field{height:34px;background:#fff;border-radius:5px;font-size:9px;color:#999;padding:0 12px;display:flex;align-items:center}
.btn-send{left:220px;top:1441px;width:102px;height:28px;border-radius:5px;background:#fff;color:var(--purple);font-size:10px;font-weight:600;display:flex;align-items:center;justify-content:center}
.appt-text{left:696px;top:1258px;width:280px;font-size:11px;line-height:16px;color:#f1ffe3}
.hours{left:696px;top:1368px;width:280px;font-size:11px;color:#fff;line-height:21px}
.hours div{display:flex}
.hours b{width:156px;font-weight:600}

/* treatments */
.tr-kicker{left:225px;top:1622px;font-family:var(--serif);font-size:16px;color:var(--purple)}
.tr-title{left:225px;top:1644px;font-family:var(--serif);font-size:26px;color:var(--purple)}
.tr-intro{left:225px;top:1700px;width:245px;font-size:14px;line-height:22px;color:#444}
.tr-item{width:200px}
.tr-item .num{font-size:12px;color:var(--green)}
.tr-item h4{font-size:12px;font-weight:500;color:var(--green);margin-top:6px}
.tr-item p{font-size:10px;line-height:15px;color:var(--muted);margin-top:6px}

/* testimonials */
.sec-title{width:1200px;left:0;text-align:center;font-family:var(--serif);font-size:24px;color:var(--purple)}
.t-back{top:2100px;width:520px;height:158px;left:338px;background:#fff;box-shadow:0 4px 18px rgba(0,0,0,.12)}
.t-card{left:398px;top:2073px;width:402px;height:211px;background:#fff;box-shadow:0 6px 24px rgba(0,0,0,.14);text-align:center;padding-top:22px}
.avatar{width:60px;height:60px;border-radius:50%;margin:0 auto;background:radial-gradient(circle at 50% 40%,#d9b8a2,#8f6552)}
.t-card h5{margin-top:12px;font-size:14px;font-weight:600;color:var(--purple)}
.t-card .role{font-size:9px;font-weight:600;letter-spacing:.5px;margin-top:2px}
.t-card p{font-size:10px;line-height:15px;color:var(--muted);width:320px;margin:10px auto 0}
.pager{top:2318px;width:24px;height:24px;border:2px solid var(--green);border-radius:3px;display:flex;align-items:center;justify-content:center}

/* posts */
.post-accent{width:120px;height:130px}
.post{top:2518px;width:241px;height:357px;background:#fff;box-shadow:0 4px 18px rgba(0,0,0,.10);padding:28px 16px 0}
.post .thumb{width:212px;height:124px}
.post h6{font-family:var(--serif);font-size:12px;font-weight:600;line-height:15px;margin-top:16px}
.post .meta{font-size:9px;color:#999;margin-top:8px}
.post .meta span{color:var(--purple)}
.post p{font-size:10px;line-height:15px;color:var(--muted);margin-top:10px}
.post .more{display:block;margin-top:18px;font-size:9px;font-weight:600;color:var(--green)}

/* footer */
.footer-bg{left:0;top:2940px;width:1200px;height:431px}
.sub-title{left:712px;top:2990px;font-family:var(--serif);font-size:21px;color:#fff}
.sub-text{left:726px;top:3020px;font-size:10px;color:#f2e6f6}
.sub-input{left:591px;top:3045px;width:341px;height:30px;border-radius:15px;background:#fff;font-size:9px;color:#aaa;padding:0 16px;display:flex;align-items:center;justify-content:space-between}
.f-head{top:3118px;font-family:var(--serif);font-size:13px;color:#fff}
.f-links{top:3158px;font-size:10px;color:#fff;line-height:30px}
.f-links li{list-style:none}
.f-links li::before{content:"› ";color:#e7c8f0}
.tweet{left:486px;width:290px;font-size:10px;line-height:15px;color:#fff;display:flex;gap:10px}
.tweet i{flex:none;width:10px;height:10px;border-radius:50%;background:#fff;margin-top:3px}
.contact{left:832px;top:3158px;font-size:10px;line-height:15px;color:#fff;width:130px}
.bottom-bar{left:0;top:3371px;width:1200px;height:38px;background:#4d2478;color:#fff;font-size:10px;display:flex;align-items:center;justify-content:space-between;padding:0 170px}
.socials{display:flex;gap:14px}
.socials i{width:12px;height:12px;background:#fff;border-radius:2px}
</style>
</head>
<body>

<!-- hero -->
<div class="abs hero-photo" role="img" aria-label="Smiling young woman sitting in a field of purple wildflowers at sunset"></div>
<svg class="abs hero-wave" viewBox="0 0 1200 145" preserveAspectRatio="none"><path d="M0 30 C300 120 650 150 1200 0 L1200 145 L0 145 Z" fill="#fff"/></svg>
<a class="abs btn-top" href="#">GET AN APPOINTMENT</a>
<div class="abs logo"><span class="logo-name">Brightmoor</span><span class="logo-dot"></span></div>
<div class="abs logo-sub">WELLNESS USA</div>
<nav class="abs nav"><a class="active" href="#">HOME</a><a href="#">ABOUT US</a><a href="#">SERVICES</a><a href="#">TREATMENT</a><a href="#">FAQS</a><a href="#">CONTACT</a></nav>
<h1 class="abs hero-title">Life is not for a moment<br>but its a combination of moments</h1>
<a class="abs btn btn-know" href="#">KNOW MORE</a>
<a class="abs btn btn-book" href="#">BOOK A SESSION</a>

<!-- welcome -->
<div class="abs welcome-kicker">welcome to</div>
<h2 class="abs welcome-title">Brightmoor</h2>

<div class="abs feature" style="left:236px">
  <div class="icon"><svg width="22" height="22" viewBox="0 0 22 22" fill="none" stroke="#6cb51c" stroke-width="1.6"><rect x="3" y="9" width="12" height="9" rx="1"/><path d="M15 11h2a2 2 0 0 1 0 4h-2M7 3v4M11 3v4"/></svg></div>
  <h3>Talking About Problems</h3>
  <p>Share what weighs on you in a calm, safe room with someone who listens closely.</p>
  <span class="arrow">→</span>
</div>
<div class="abs feature is-active" style="left:486px">
  <div class="icon"><svg width="22" height="22" viewBox="0 0 22 22" fill="none" stroke="#fff" stroke-width="1.6"><path d="M3 4h11v8H8l-3 3v-3H3z"/><path d="M14 8h5v8h-2v3l-3-3h-4v-2"/></svg></div>
  <h3>Ongoing Discussion</h3>
  <p>Regular sessions help you track progress and adjust care at a pace that suits you.</p>
  <span class="arrow">→</span>
</div>
<div class="abs feature" style="left:745px">
  <div class="icon"><svg width="22" height="22" viewBox="0 0 22 22" fill="none" stroke="#6cb51c" stroke-width="1.6"><circle cx="10" cy="12" r="7"/><circle cx="10" cy="12" r="3"/><path d="M10 12l8-8M15 4h3v3"/></svg></div>
  <h3>Solving the Problem.</h3>
  <p>Together we build a clear plan with practical steps toward lasting relief.</p>
  <span class="arrow">→</span>
</div>

<!-- appointment band -->
<svg class="abs band" viewBox="0 0 1200 472" preserveAspectRatio="none">
  <defs><linearGradient id="laptopTone" x1="0" y1="0" x2="1" y2="1"><stop offset="0" stop-color="#8a5bb3"/><stop offset="1" stop-color="#5f2f8a"/></linearGradient></defs>
  <rect x="0" y="0" width="659" height="472" fill="url(#laptopTone)" role="img" aria-label="Hands typing on a laptop, tinted purple"/>
  <rect x="659" y="0" width="541" height="472" fill="#6cb51c"/>
  <path d="M0 0 L1200 0 L1200 12 C850 90 420 60 0 0 Z" fill="#fff"/>
  <path d="M0 420 C350 470 800 480 1200 380 L1200 472 L0 472 Z" fill="#fff"/>
</svg>
<div class="abs band-kicker" style="left:222px;top:1184px">When you</div>
<div class="abs band-title" style="left:222px;top:1203px">Can Visit Us</div>
<div class="abs field" style="left:220px;top:1260px;width:366px">Name</div>
<div class="abs field" style="left:220px;top:1298px;width:180px">Email</div>
<div class="abs field" style="left:406px;top:1298px;width:180px">Phone</div>
<div class="abs field" style="left:220px;top:1336px;width:180px">Subject</div>
<div class="abs field" style="left:406px;top:1336px;width:180px">Available Date</div>
<div class="abs field" style="left:220px;top:1374px;width:366px;height:58px;align-items:flex-start;padding-top:10px">Subject to discuss</div>
<a class="abs btn-send" href="#">SEND</a>

<div class="abs band-kicker" style="left:696px;top:1184px">Make</div>
<div class="abs band-title" style="left:696px;top:1203px">An Appointment</div>
<p class="abs appt-text">Book a first visit with our care team. We will call you back within one working day to confirm a time that fits your week.</p>
<div class="abs hours">
  <div><b>Monday - Friday</b>9.15 am - 5.30 pm</div>
  <div><b>Saturday</b>Closed</div>
  <div><b>Sunday</b>Closed</div>
</div>

<!-- treatments -->
<div class="abs tr-kicker">Our</div>
<h2 class="abs tr-title">Treatments</h2>
<p class="abs tr-intro">Treatment we make with knowledge and passion. Gentle care tailored to you, guided by experience. Each plan respects your pace, your story, and your goals.</p>

<div class="abs tr-item" style="left:523px;top:1625px"><div class="num">01</div><h4>Chronic Pain</h4><p>Relief for long-lasting pain that affects sleep, mood and daily life.</p></div>
<div class="abs tr-item" style="left:750px;top:1625px"><div class="num">02</div><h4>PTSD</h4><p>Supportive care for trauma, built on trust and a calm setting.</p></div>
<div class="abs tr-item" style="left:523px;top:1735px"><div class="num">03</div><h4>Major Depression</h4><p>Evidence-based options when other treatments have not helped.</p></div>
<div class="abs tr-item" style="left:750px;top:1735px"><div class="num">04</div><h4>Anxiety Therapy</h4><p>Tools and treatment to ease worry and restore a sense of calm.</p></div>
<div class="abs tr-item" style="left:523px;top:1847px"><div class="num">05</div><h4>Hypnotherapy</h4><p>Guided relaxation sessions to help you reset habits and thoughts.</p></div>
<div class="abs tr-item" style="left:750px;top:1847px"><div class="num">06</div><h4>IV Nutrition Therapy</h4><p>Vitamin infusions that support energy, focus and recovery.</p></div>

<!-- testimonials -->
<h2 class="abs sec-title" style="top:2003px">What People are Saying</h2>
<div class="abs t-back"></div>
<div class="abs t-card">
  <div class="avatar" role="img" aria-label="Portrait photo of the client"></div>
  <h5>Mara Ellison</h5>
  <div class="role">CEO OF LUMEN STUDIO</div>
  <p>The team made me feel heard from the first call. For the first time in years I feel hopeful and steady again. Thank you for your patience.</p>
</div>
<div class="abs pager" style="left:570px"><svg width="8" height="10" viewBox="0 0 8 10"><path d="M6 1L2 5l4 4" stroke="#6cb51c" stroke-width="2" fill="none"/></svg></div>
<div class="abs pager" style="left:604px"><svg width="8" height="10" viewBox="0 0 8 10"><path d="M2 1l4 4-4 4" stroke="#6cb51c" stroke-width="2" fill="none"/></svg></div>

<!-- latest posts -->
<h2 class="abs sec-title" style="top:2438px">Latest Post</h2>
<div class="abs post-accent" style="left:341px;top:2502px;background:var(--violet)"></div>
<div class="abs post-accent" style="left:591px;top:2502px;background:var(--green)"></div>
<div class="abs post-accent" style="left:840px;top:2502px;background:var(--yellow)"></div>

<article class="abs post" style="left:220px">
  <div class="thumb" role="img" aria-label="Group of women talking in a bright room" style="background:linear-gradient(135deg,#e9ecef,#b8c2c9)"></div>
  <h6>Depression effects childrens mental development</h6>
  <div class="meta">Stress Management | By <span>Admin</span></div>
  <p>Early signs in children are easy to miss. Learn what to watch for and how gentle support at home can help.</p>
  <a class="more" href="#">Read More</a>
</article>
<article class="abs post" style="left:470px">
  <div class="thumb" role="img" aria-label="Close-up of a woman resting her head on her hand" style="background:linear-gradient(135deg,#6b6f3a,#2f3320)"></div>
  <h6>Depression effects childrens mental development</h6>
  <div class="meta">Stress Management | By <span>Admin</span></div>
  <p>Early signs in children are easy to miss. Learn what to watch for and how gentle support at home can help.</p>
  <a class="more" href="#">Read More</a>
</article>
<article class="abs post" style="left:720px">
  <div class="thumb" role="img" aria-label="Black and white photo of a person sitting alone" style="background:linear-gradient(135deg,#d6d6d6,#6e6e6e)"></div>
  <h6>Depression effects childrens mental development</h6>
  <div class="meta">Stress Management | By <span>Admin</span></div>
  <p>Early signs in children are easy to miss. Learn what to watch for and how gentle support at home can help.</p>
  <a class="more" href="#">Read More</a>
</article>

<!-- footer -->
<svg class="abs footer-bg" viewBox="0 0 1200 431" preserveAspectRatio="none">
  <defs><linearGradient id="footTone" x1="0" y1="0" x2="0" y2="1"><stop offset="0" stop-color="#7c1f86"/><stop offset="1" stop-color="#5a2f8f"/></linearGradient></defs>
  <path d="M0 120 C400 40 850 -20 1200 30 L1200 431 L0 431 Z" fill="url(#footTone)"/>
</svg>
<div class="abs sub-title">Subscribe Newsletter</div>
<div class="abs sub-text">Get our news, updates, success stories</div>
<div class="abs sub-input">Type your email id <svg width="14" height="11" viewBox="0 0 14 11" fill="none" stroke="#6a2c91" stroke-width="1.4"><rect x="1" y="1" width="12" height="9"/><path d="M1 1l6 5 6-5"/></svg></div>

<div class="abs f-head" style="left:177px">Useful Links</div>
<ul class="abs f-links" style="left:189px"><li>Home</li><li>About Us</li><li>History</li><li>Contact</li><li>Blog</li></ul>
<ul class="abs f-links" style="left:309px"><li>Book Session</li><li>Services</li><li>FAQs</li><li>Success Stories</li></ul>

<div class="abs f-head" style="left:486px">Twitter Feed</div>
<div class="abs tweet" style="top:3158px"><i></i><div>Harbor Lane Press - Calm mind weekly notes on rest, routine and care, simple and useful for every reader...<br>yesterday</div></div>
<div class="abs tweet" style="top:3232px"><i></i><div>Harbor Lane Press - Calm mind weekly notes on rest, routine and care, simple and useful for every reader...<br>yesterday</div></div>

<div class="abs f-head" style="left:832px">Contact Info</div>
<div class="abs contact">48 Palm Grove Ave, Sarasota, FL, USA<br><br>+1 941 555 0142<br>+1 941 555 0187<br><br>info@brightmoorwellness.com<br>www.brightmoorwellness.com</div>

<div class="abs bottom-bar"><span>©2019, All Right Reserved BRIGHTMOOR</span><div class="socials"><i></i><i></i><i></i><i></i><i></i></div></div>

</body>
</html>
```